AI Layout work for Business Cards, Letterhead and Compliment Slip for Award-winning UK Property Deve

No actual logo or corporate identity design work needed here but some skill required to create layouts for business card, letterhead and compliment slip for this award-winning company.
I can provide AI files featuring the company logo and an initial layout of the business card, (6 versions featuring the same design but for different personnel), along with some initial instructions (with possibly more to follow from the client). The finished layouts for each item need to be print-ready in AI format - 8 in all (6 for each business card plus 1 for letterhead and 1 for compliment slip).
I've given this project a 5-day duration but there may be some flexibility built into that depending on client feedback. Hopefully that won't be a problem.
UPDATE:
The client has been very prescriptive about the layout and design of these. To that end, please find 3 additional pdfs that explain what's required.
1.
All BUSINESS CARDS need to be laid out as per the attached AI file (but see latest pdf to check which layout - there are 2 in the original AI file). Use the details in the RUNE-contact-details.pdf to create 6 individual AI files, one for each card.
2.
Create 2 additional AI files, one each for the LETTERHEAD and the COMPLIMENT SLIP based on the latest mock-up that I've provided (letterhead-layout-final.pdf)
In all, I need EIGHT individual AI files, 6 for each business card, 1 for the letterhead and 1 for the compliment slip. I'd like to get this done as soon as possible now please.
Target Market(s)
Purchasers of upmarket luxury properties - see here: http://www.runeestates.co.uk
Industry/Entity Type
Business
Requirements
Must have
- Layouts need to be cool, understated and uncluttered.
Nice to have
- Please keep it simple! The actual logo background colour is likely to change (awaiting confirmation from client) but accompanying text detail and font (Deja Vu Sans Condensed) can remain as seen in the files below - for the time being at least! That having been said, I'm open to suggestions.
Should not have
- Nothing extreme or ostentatious please.

```html
<!DOCTYPE html>
<html lang="en">
<head>
<meta charset="utf-8">
<title>RUNE Stationery – Business Card, Letterhead, Compliment Slip</title>
<link rel="stylesheet" href="https://fonts.googleapis.com/css2?family=PT+Sans+Narrow:wght@400;700&display=swap">
<style>
  :root {
    --navy: #1b2352;
    --navy-deep: #141a3f;
    --swoosh: #ececee;
    --swoosh-dark: #d9d9dd;
    --paper: #ffffff;
    --ink: #2a2d3a;
    --stage: #e7e8ec;
    --rule: #9aa0b8;
  }
  * { box-sizing: border-box; margin: 0; padding: 0; }
  html, body { width: 1200px; height: 800px; overflow: hidden; }
  body {
    background: var(--stage);
    font-family: "PT Sans Narrow", "Arial Narrow", sans-serif;
    color: var(--ink);
    position: relative;
  }
  .sheet {
    position: absolute;
    background: var(--paper);
    overflow: hidden;
    box-shadow: 0 3px 14px rgba(20, 26, 63, .18);
  }
  .sheet svg.art { position: absolute; inset: 0; width: 100%; height: 100%; }
  .brand-name {
    position: absolute;
    color: var(--navy);
    font-weight: 700;
    letter-spacing: .04em;
    line-height: 1;
  }
  .address { position: absolute; text-align: right; line-height: 1.35; color: var(--ink); }
  .address span { display: block; }
  .icon { width: 1em; height: 1em; vertical-align: -0.12em; margin-right: .35em; }

  /* Business card */
  .business-card { left: 40px; top: 290px; width: 340px; height: 221px; }
  .business-card .watermark-name {
    position: absolute; left: 10px; top: 6px;
    font-size: 40px; letter-spacing: .18em;
    color: rgba(255, 255, 255, .09); white-space: nowrap;
  }
  .business-card .person-name {
    position: absolute; right: 14px; top: 22px;
    color: #fff; font-size: 16px;
  }
  .business-card .person-role {
    position: absolute; right: 14px; top: 52px;
    color: #fff; font-size: 12px;
  }
  .business-card .contact-list {
    position: absolute; left: 16px; top: 92px;
    list-style: none; font-size: 12px; line-height: 18px; color: var(--ink);
  }
  .business-card .contact-list .icon { fill: var(--ink); }
  .business-card .address { right: 16px; top: 88px; font-size: 12px; line-height: 17px; }
  .business-card .brand-name { left: 16px; top: 184px; font-size: 24px; }

  /* Letterhead */
  .letterhead { left: 410px; top: 103px; width: 420px; height: 594px; }
  .letterhead .brand-name { left: 22px; top: 22px; font-size: 34px; }
  .letterhead .address { right: 14px; top: 10px; font-size: 8.5px; line-height: 12px; }
  .letterhead .footer-contacts {
    position: absolute; left: 0; right: 0; bottom: 10px;
    display: flex; justify-content: space-between; align-items: center;
    padding: 0 16px; color: #fff; font-size: 10px; list-style: none;
  }
  .letterhead .footer-contacts li:nth-child(2) { margin-top: -14px; }
  .letterhead .footer-contacts li:first-child { margin-top: -34px; }
  .letterhead .footer-contacts .icon { fill: #fff; }

  /* Compliment slip */
  .compliment-slip { left: 860px; top: 330px; width: 300px; height: 142px; }
  .compliment-slip .brand-name { left: 14px; top: 12px; font-size: 24px; }
  .compliment-slip .address { right: 10px; top: 5px; font-size: 7px; line-height: 9.5px; }
  .compliment-slip .compliments-band {
    position: absolute; left: 0; right: 0; bottom: 0; height: 16px;
    background: var(--navy); color: #fff;
    font-size: 8px; letter-spacing: .3em; text-align: right;
    padding-right: 10px; line-height: 16px;
  }
</style>
</head>
<body>

<!-- Business card front -->
<section class="sheet business-card" aria-label="Business card">
  <svg class="art" viewBox="0 0 340 221" preserveAspectRatio="none" aria-hidden="true">
    <polygon fill="var(--navy)" points="0,0 340,0 340,72 268,72 260,80 252,72 236,72 236,50 0,50"/>
    <line x1="170" y1="86" x2="170" y2="182" stroke="var(--rule)" stroke-width="1"/>
    <path fill="var(--swoosh)" d="M0,200 C90,188 220,186 340,196 L340,221 L0,221 Z"/>
  </svg>
  <div class="watermark-name" aria-hidden="true">Oliver Hart</div>
  <div class="person-name">Oliver Hart</div>
  <div class="person-role">Director</div>
  <ul class="contact-list">
    <li><svg class="icon" viewBox="0 0 16 16"><circle cx="8" cy="8" r="7" fill="none" stroke="currentColor" stroke-width="1.4"/><ellipse cx="8" cy="8" rx="3" ry="7" fill="none" stroke="currentColor" stroke-width="1.2"/><line x1="1" y1="8" x2="15" y2="8" stroke="currentColor" stroke-width="1.2"/></svg>runeestates.co.uk</li>
    <li><svg class="icon" viewBox="0 0 16 16"><rect x="4" y="1" width="8" height="14" rx="1.5"/><rect x="5.5" y="3" width="5" height="7" fill="#fff"/></svg>+44 (0)1632 960418</li>
    <li><svg class="icon" viewBox="0 0 16 16"><rect x="1" y="3" width="14" height="10" rx="1"/><path d="M1.5 3.8 L8 9 L14.5 3.8" fill="none" stroke="#fff" stroke-width="1.3"/></svg>enquiries@runeestates.co.uk</li>
  </ul>
  <address class="address">
    <span>RUNE Exclusive Properties</span>
    <span>Elm Court House</span>
    <span>Elm Court Lane</span>
    <span>Ashby Wells</span>
    <span>AW4 2RT</span>
  </address>
  <div class="brand-name">RUNE</div>
</section>

<!-- Letterhead -->
<section class="sheet letterhead" aria-label="Letterhead">
  <svg class="art" viewBox="0 0 420 594" preserveAspectRatio="none" aria-hidden="true">
    <path fill="var(--swoosh)" d="M0,74 C120,58 260,30 420,22 L420,34 C270,40 130,66 0,86 Z"/>
    <line x1="132" y1="18" x2="132" y2="82" stroke="var(--rule)" stroke-width="1"/>
    <path fill="var(--swoosh-dark)" d="M0,488 C110,530 250,556 420,536 L420,560 L0,560 Z"/>
    <path fill="var(--navy)" d="M0,496 C110,540 250,566 420,548 L420,594 L0,594 Z"/>
  </svg>
  <div class="brand-name">RUNE</div>
  <address class="address">
    <span>RUNE Exclusive Properties</span>
    <span>Elm Court House</span>
    <span>Elm Court Lane</span>
    <span>Ashby Wells</span>
    <span>AW4 2RT</span>
  </address>
  <ul class="footer-contacts">
    <li><svg class="icon" viewBox="0 0 16 16"><rect x="4" y="1" width="8" height="14" rx="1.5"/><rect x="5.5" y="3" width="5" height="7" fill="var(--navy)"/></svg>+44 (0)1632 960418</li>
    <li><svg class="icon" viewBox="0 0 16 16"><rect x="1" y="3" width="14" height="10" rx="1"/><path d="M1.5 3.8 L8 9 L14.5 3.8" fill="none" stroke="var(--navy)" stroke-width="1.3"/></svg>enquiries@runeestates.co.uk</li>
    <li><svg class="icon" viewBox="0 0 16 16"><circle cx="8" cy="8" r="7" fill="none" stroke="#fff" stroke-width="1.4"/><ellipse cx="8" cy="8" rx="3" ry="7" fill="none" stroke="#fff" stroke-width="1.2"/><line x1="1" y1="8" x2="15" y2="8" stroke="#fff" stroke-width="1.2"/></svg>runeestates.co.uk</li>
  </ul>
</section>

<!-- Compliment slip -->
<section class="sheet compliment-slip" aria-label="Compliment slip">
  <div class="brand-name">RUNE</div>
  <address class="address">
    <span>RUNE Exclusive Properties</span>
    <span>Elm Court House</span>
    <span>Elm Court Lane</span>
    <span>Ashby Wells</span>
    <span>AW4 2RT</span>
  </address>
  <div class="compliments-band">With Compliments</div>
</section>

</body>
</html>
```